High-End Bifold Brochure for Aesthetics Medspa Business

I need a print-ready, bifold brochure designed for a high-end, luxurious Aesthetics/Medspa practice.

The brochure will showcase the latest IV Therapy content (6 options included in MENU.docx), and exclusive Vitamin B12+ wellness shot content (included in LS PDF). It should also include the business logo and basic office contact options.

The design should be clean, modern, and appealing with a light design. It should flow nicely and compliment the website theme/design. Preferably, having the 6 IV treatments inside bifold, with B12 shot on back/outside page. For easy viewing.

I have attached a few licensed images, if you think they will incorporate into the design nicely. Otherwise, please ignore them. If needed, I can send more.

https://lunavelleskincareclinic.com/
Brand purple: #491c64
Fonts used on site:
Josefin Sans
Montserrat

Size should be 6.5 x 9 using specs on Quillapress's template page (Half Fold design)
https://www.quillapress.com/resources/templates

• Montserrat, Josefin Sans, or similar

• Content included in MENU + B12 shot content on PDF.
Similar feel to the website, High-end, modern, luxurious

```html
<!DOCTYPE html>
<html lang="en">
<head>
<meta charset="utf-8">
<title>Lunavelle Skincare – IV Therapy Brochure</title>
<link rel="stylesheet" href="https://fonts.googleapis.com/css2?family=Josefin+Sans:wght@400;600;700&family=Montserrat:wght@400;500;600;700&family=Oswald:wght@500;600&display=swap">
<style>
  :root {
    --purple: #491c64;
    --purple-mid: #5c2a80;
    --purple-light: #8a4bc0;
    --orange: #f39a3b;
    --orange-light: #f8c26a;
    --ink: #2b2b2b;
    --body: #444;
    --paper: #f5f5f6;
    --backdrop: #7a7a7a;
    --white: #ffffff;
  }
  * { margin: 0; padding: 0; box-sizing: border-box; }
  html, body { width: 1200px; height: 824px; overflow: hidden; }
  body { background: var(--backdrop); font-family: "Montserrat", sans-serif; position: relative; }

  .page { position: absolute; top: 66px; width: 503px; height: 693px; overflow: hidden; }
  .page--cover { left: 63px; background: var(--paper); }
  .page--inside { left: 622px; background: linear-gradient(90deg, #ececec 0%, #f7f7f7 49.9%, #f2f2f2 50%, #fafafa 100%); }
  .page--inside::after { content: ""; position: absolute; left: 0; right: 0; bottom: 0; height: 3px; background: var(--purple-light); }
  .cover-art { position: absolute; inset: 0; }

  .abs { position: absolute; }

  /* Cover */
  .call-line { left: 37px; top: 29px; font-family: "Oswald", sans-serif; font-weight: 500; font-size: 15px; color: var(--ink); letter-spacing: .3px; }
  .call-strong { left: 37px; top: 44px; font-family: "Oswald", sans-serif; font-weight: 600; font-size: 25px; color: var(--ink); line-height: 1; }
  .phone-pill { left: 31px; top: 82px; width: 194px; height: 26px; background: var(--purple); border-radius: 13px; }
  .phone-icon { left: 31px; top: 79px; width: 32px; height: 32px; border-radius: 50%; background: var(--white); border: 2px solid var(--purple); }
  .phone-number { left: 72px; top: 85px; font-family: "Josefin Sans", sans-serif; font-weight: 700; font-size: 18px; color: var(--white); }

  .brand-mark { left: 290px; top: 30px; width: 48px; height: 48px; border-radius: 50%; border: 2px solid var(--purple); }
  .brand-name { left: 350px; top: 42px; font-family: "Josefin Sans", sans-serif; font-weight: 600; font-size: 16px; line-height: 1.2; color: var(--purple); letter-spacing: .5px; }

  .address { left: 0; width: 251px; top: 607px; text-align: center; color: var(--white); font-size: 9.5px; line-height: 1.4; font-weight: 400; }
  .pin { left: 121px; top: 593px; }
  .email { left: 0; width: 251px; top: 641px; text-align: center; color: var(--white); font-size: 9.5px; }
  .social { left: 93px; top: 659px; display: flex; gap: 4px; }
  .social span { width: 15px; height: 15px; border-radius: 50%; background: var(--white); }

  .tagline { left: 251px; width: 252px; text-align: center; color: var(--white); font-family: "Josefin Sans", sans-serif; font-weight: 700; }
  .tagline--city { top: 574px; font-size: 37px; letter-spacing: 1px; }
  .tagline--sub { top: 616px; font-size: 20px; letter-spacing: .5px; }
  .tagline-rule { left: 335px; top: 647px; width: 79px; height: 1px; background: var(--white); }
  .website { left: 251px; width: 252px; top: 659px; text-align: center; color: var(--white); font-size: 9.5px; letter-spacing: .6px; }

  /* Inside */
  .menu-title { left: 21px; top: 22px; font-family: "Josefin Sans", sans-serif; font-weight: 700; font-size: 18.5px; color: var(--ink); letter-spacing: .6px; }
  .menu-bar { left: 21px; top: 46px; width: 205px; height: 23px; background: var(--purple); color: var(--white); font-family: "Josefin Sans", sans-serif; font-weight: 700; font-size: 18px; letter-spacing: 5px; text-align: center; line-height: 26px; }

  .treatment-head { left: 21px; width: 205px; height: 24px; }
  .treatment-head svg { position: absolute; left: 0; top: 0; }
  .treatment-name { position: absolute; left: 0; bottom: 4px; font-family: "Montserrat", sans-serif; font-weight: 600; font-size: 10.6px; line-height: 1.25; color: var(--purple); letter-spacing: .2px; }
  .treatment-price { position: absolute; left: 150px; width: 55px; top: 4px; text-align: center; font-family: "Montserrat", sans-serif; font-weight: 700; font-size: 12.5px; color: var(--white); }
  .treatment-desc { left: 21px; width: 205px; font-size: 7.6px; line-height: 1.37; color: var(--body); text-align: justify; }

  .b12-title { left: 277px; top: 22px; font-family: "Josefin Sans", sans-serif; font-weight: 700; font-size: 18.5px; color: var(--ink); letter-spacing: .4px; }
  .b12-bar { left: 273px; top: 47px; width: 211px; height: 36px; background: var(--purple); color: var(--white); font-family: "Josefin Sans", sans-serif; font-weight: 700; font-size: 10.6px; line-height: 1.3; padding: 6px 0 0 10px; }

  .nutrient { left: 277px; width: 207px; padding-left: 12px; font-size: 7.3px; line-height: 1.42; color: var(--body); }
  .nutrient b { color: var(--purple); font-weight: 600; }
  .nutrient svg { position: absolute; left: 0; top: 1px; }

  .benefits-title { left: 273px; top: 452px; font-family: "Montserrat", sans-serif; font-weight: 600; font-size: 10.6px; color: var(--purple); letter-spacing: .3px; }
  .benefits-rule { left: 272px; top: 452px; }
  .benefit { left: 273px; width: 211px; padding-left: 13px; font-size: 7.6px; line-height: 1.37; color: var(--body); }
  .benefit svg { position: absolute; left: 0; top: 1px; }
</style>
</head>
<body>

<section class="page page--cover">
  <svg class="cover-art" width="503" height="693" viewBox="0 0 503 693">
    <defs>
      <linearGradient id="portraitTone" x1="0" y1="0" x2="1" y2="1">
        <stop offset="0" stop-color="#8c8580"/>
        <stop offset=".45" stop-color="#d9b9a5"/>
        <stop offset="1" stop-color="#e8cdb9"/>
      </linearGradient>
      <linearGradient id="staffTone" x1="0" y1="0" x2="1" y2="1">
        <stop offset="0" stop-color="#d9d3cf"/>
        <stop offset=".5" stop-color="#a97a62"/>
        <stop offset="1" stop-color="#3a3336"/>
      </linearGradient>
      <linearGradient id="orangeWave" x1="0" y1="0" x2="1" y2="0">
        <stop offset="0" stop-color="var(--orange-light)"/>
        <stop offset=".6" stop-color="var(--orange)"/>
        <stop offset="1" stop-color="#e46f2b"/>
      </linearGradient>
      <linearGradient id="purpleWave" x1="0" y1="0" x2="1" y2="0">
        <stop offset="0" stop-color="var(--purple)"/>
        <stop offset="1" stop-color="var(--purple-light)"/>
      </linearGradient>
    </defs>
    <rect x="251" y="0" width="252" height="693" fill="#fbfbfb"/>
    <g role="img" aria-label="Photo of a woman with clear skin touching her face in a bright clinic">
      <rect x="0" y="95" width="503" height="510" fill="url(#portraitTone)"/>
    </g>
    <path d="M0,0 H503 V112 C420,92 340,120 250,148 C160,175 70,150 0,98 Z" fill="var(--paper)"/>
    <path d="M251,0 H503 V112 C420,92 340,120 251,148 Z" fill="#fbfbfb"/>
    <path d="M0,98 C70,150 160,175 250,148 C340,120 420,92 503,112 V122 C420,110 340,140 250,178 C160,205 70,175 0,118 Z" fill="url(#purpleWave)"/>
    <g role="img" aria-label="Photo of a smiling medspa practitioner with a client">
      <circle cx="102" cy="379" r="104" fill="url(#staffTone)"/>
    </g>
    <circle cx="102" cy="379" r="106" fill="none" stroke="var(--purple)" stroke-width="6"/>
    <path d="M0,560 C120,520 230,480 300,488 C400,495 460,540 503,575 V600 C450,570 380,522 300,516 C200,510 100,555 0,582 Z" fill="url(#orangeWave)"/>
    <path d="M0,578 C100,550 200,522 300,520 C390,522 450,560 503,592 V693 H0 Z" fill="var(--purple)"/>
  </svg>

  <p class="abs call-line">CALL TODAY FOR YOUR</p>
  <p class="abs call-strong">FREE CONSULTATION</p>
  <div class="abs phone-pill"></div>
  <div class="abs phone-icon">
    <svg width="28" height="28" viewBox="0 0 28 28"><path d="M9 7 L12 10 L10.5 12 C11.5 14.5 13.5 16.5 16 17.5 L18 16 L21 19 L19 21.5 C13 21 7 15 6.5 9 Z" fill="none" stroke="var(--purple)" stroke-width="1.4" stroke-linejoin="round"/></svg>
  </div>
  <p class="abs phone-number">(555) 014-2380</p>

  <div class="abs brand-mark"></div>
  <p class="abs brand-name">LUNAVELLE<br>SKINCARE</p>

  <svg class="abs pin" width="14" height="14" viewBox="0 0 14 14"><path d="M7 1.5 C4.5 1.5 3 3.3 3 5.3 C3 8 7 12 7 12 C7 12 11 8 11 5.3 C11 3.3 9.5 1.5 7 1.5 Z" fill="none" stroke="var(--white)" stroke-width="1.1"/><circle cx="7" cy="5.3" r="1.4" fill="var(--white)"/></svg>
  <p class="abs address">2210 N Cedar Ridge Rd, Unit 4<br>Tucson, Arizona 85719</p>
  <p class="abs email">&#9993; info@lunavelleskincareclinic.com</p>
  <div class="abs social"><span></span><span></span><span></span><span></span></div>

  <p class="abs tagline tagline--city">TUCSON'S</p>
  <p class="abs tagline tagline--sub">PREMIER MEDSPA</p>
  <div class="abs tagline-rule"></div>
  <p class="abs website">www.<b>LunavelleSkincareClinic</b>.com</p>
</section>

<section class="page page--inside">
  <h1 class="abs menu-title">THE VITAL DRIP</h1>
  <p class="abs menu-bar">IV THERAPY</p>

  <div class="abs treatment-head" style="top:86px">
    <svg width="205" height="24"><polyline points="0,23 118,23 130,8 150,8" fill="none" stroke="var(--purple)" stroke-width=".8"/><polygon points="157,2 205,2 205,22 150,22" fill="var(--purple)"/></svg>
    <p class="treatment-name">IMMUNITY BOOSTER</p><p class="treatment-price">$150</p>
  </div>
  <p class="abs treatment-desc" style="top:120px">Have a cold, flu or just need to give your immunity a boost? Let us mix a powerful punch in our booster bag just for you to prevent or relieve aches and pain</p>

  <div class="abs treatment-head" style="top:165px">
    <svg width="205" height="24"><polyline points="0,23 118,23 130,8 150,8" fill="none" stroke="var(--purple)" stroke-width=".8"/><polygon points="157,2 205,2 205,22 150,22" fill="var(--purple)"/></svg>
    <p class="treatment-name">REFRESH &amp; HYDRATE</p><p class="treatment-price">$100</p>
  </div>
  <p class="abs treatment-desc" style="top:200px">Relieve dehydration from the extremes of lifestyle with our balanced electrolyte cocktail targeting jet lag, fatigue, stress and sports related activity to leave you feeling more youthful and refreshed!</p>

  <div class="abs treatment-head" style="top:256px">
    <svg width="205" height="24"><polyline points="0,23 118,23 130,8 150,8" fill="none" stroke="var(--purple)" stroke-width=".8"/><polygon points="157,2 205,2 205,22 150,22" fill="var(--purple)"/></svg>
    <p class="treatment-name">MIGRAINE BUSTER</p><p class="treatment-price">$150</p>
  </div>
  <p class="abs treatment-desc" style="top:290px">Eradicate your migraine pain, nausea, vomiting, and light sensitivity with our magic formula</p>

  <div class="abs treatment-head" style="top:329px">
    <svg width="205" height="24"><polyline points="0,23 118,23 130,8 150,8" fill="none" stroke="var(--purple)" stroke-width=".8"/><polygon points="157,2 205,2 205,22 150,22" fill="var(--purple)"/></svg>
    <p class="treatment-name">WELLNESS INFUSION:<br>Myer's Cocktail</p><p class="treatment-price">$180</p>
  </div>
  <p class="abs treatment-desc" style="top:364px">This infusion of vitamins, minerals and electrolytes results in direct access of these nutrients into your cells, enhancing energy, decreasing stress and anxiety in addition to improving memory. Other benefits include relief of asthma, depression, allergies and fibromyalgia pain</p>

  <div class="abs treatment-head" style="top:432px">
    <svg width="205" height="24"><polyline points="0,23 118,23 130,8 150,8" fill="none" stroke="var(--purple)" stroke-width=".8"/><polygon points="157,2 205,2 205,22 150,22" fill="var(--purple)"/></svg>
    <p class="treatment-name">GLO</p><p class="treatment-price">$200</p>
  </div>
  <p class="abs treatment-desc" style="top:467px">A Beauty mixture of Glutathione, Biotin and our special formula created to strengthen your hair, nails and skin for that SPECIAL LOOK!</p>

  <div class="abs treatment-head" style="top:517px">
    <svg width="205" height="24"><polyline points="0,23 118,23 130,8 150,8" fill="none" stroke="var(--purple)" stroke-width=".8"/><polygon points="157,2 205,2 205,22 150,22" fill="var(--purple)"/></svg>
    <p class="treatment-name">THE ULTIMATE WEIGHT<br>LOSS INFUSION</p><p class="treatment-price">$180</p>
  </div>
  <p class="abs treatment-desc" style="top:552px">Our unique fat burning formula targets fatty deposits resulting in fat expulsion from the body resulting in a more defined and contoured appearance.</p>

  <div class="abs treatment-head" style="top:603px">
    <svg width="205" height="24"><polyline points="0,23 118,23 130,8 150,8" fill="none" stroke="var(--purple)" stroke-width=".8"/><polygon points="157,2 205,2 205,22 150,22" fill="var(--purple)"/></svg>
    <p class="treatment-name">NAD+ IV: THE FOUNTAIN<br>OF YOUTH (+-)</p><p class="treatment-price">$350</p>
  </div>
  <p class="abs treatment-desc" style="top:638px">Anti-aging co-enzyme NAD+ in conjunction with Vitamins elevates brain health and beauty, all in one IV treatment!</p>

  <h2 class="abs b12-title">DR. HALBROOK'S</h2>
  <p class="abs b12-bar">VITAMIN B12 COCKTAIL'S<br>ESSENTIAL VITAMINS &amp; NUTRIENTS:</p>

  <p class="abs nutrient" style="top:96px"><svg width="9" height="9" viewBox="0 0 9 9"><circle cx="4.5" cy="4.5" r="3.9" fill="none" stroke="var(--purple)" stroke-width=".8"/><path d="M2.7 4.6 L4 5.9 L6.4 3.3" fill="none" stroke="var(--purple)" stroke-width=".8"/></svg><b>Thiamine -</b> is used by the body to metabolize food for energy and maintain proper health and nerve function.</p>
  <p class="abs nutrient" style="top:138px"><svg width="9" height="9" viewBox="0 0 9 9"><circle cx="4.5" cy="4.5" r="3.9" fill="none" stroke="var(--purple)" stroke-width=".8"/><path d="M2.7 4.6 L4 5.9 L6.4 3.3" fill="none" stroke="var(--purple)" stroke-width=".8"/></svg><b>Riboflavin-</b> acts as an antioxidant within the body. Riboflavin prevents free radical damage and protects skin and eye health.</p>
  <p class="abs nutrient" style="top:180px"><svg width="9" height="9" viewBox="0 0 9 9"><circle cx="4.5" cy="4.5" r="3.9" fill="none" stroke="var(--purple)" stroke-width=".8"/><path d="M2.7 4.6 L4 5.9 L6.4 3.3" fill="none" stroke="var(--purple)" stroke-width=".8"/></svg><b>Niacinamide -</b> helps maintain a healthy cardiovascular system and metabolism, brain function, healthy skin formation, and aids in the prevention of and management of diabetes.</p>
  <p class="abs nutrient" style="top:233px"><svg width="9" height="9" viewBox="0 0 9 9"><circle cx="4.5" cy="4.5" r="3.9" fill="none" stroke="var(--purple)" stroke-width=".8"/><path d="M2.7 4.6 L4 5.9 L6.4 3.3" fill="none" stroke="var(--purple)" stroke-width=".8"/></svg><b>Pyridoxine -</b> is important for brain development and keeping the nervous and immune systems healthy.</p>
  <p class="abs nutrient" style="top:265px"><svg width="9" height="9" viewBox="0 0 9 9"><circle cx="4.5" cy="4.5" r="3.9" fill="none" stroke="var(--purple)" stroke-width=".8"/><path d="M2.7 4.6 L4 5.9 L6.4 3.3" fill="none" stroke="var(--purple)" stroke-width=".8"/></svg><b>Hydroxocobalamin -</b> helps with DNA synthesis and supports replication, it also helps in the body's use of fats and carbohydrates for energy, and in the making of new proteins.</p>
  <p class="abs nutrient" style="top:318px"><svg width="9" height="9" viewBox="0 0 9 9"><circle cx="4.5" cy="4.5" r="3.9" fill="none" stroke="var(--purple)" stroke-width=".8"/><path d="M2.7 4.6 L4 5.9 L6.4 3.3" fill="none" stroke="var(--purple)" stroke-width=".8"/></svg><b>Methionine -</b> aids in tissue growth and repair, as well as promoting healthy hair, skin, and nails.</p>
  <p class="abs nutrient" style="top:351px"><svg width="9" height="9" viewBox="0 0 9 9"><circle cx="4.5" cy="4.5" r="3.9" fill="none" stroke="var(--purple)" stroke-width=".8"/><path d="M2.7 4.6 L4 5.9 L6.4 3.3" fill="none" stroke="var(--purple)" stroke-width=".8"/></svg><b>Inositol -</b> aids in the metabolic breakdown of fats, and helps reduce blood cholesterol.</p>
  <p class="abs nutrient" style="top:384px"><svg width="9" height="9" viewBox="0 0 9 9"><circle cx="4.5" cy="4.5" r="3.9" fill="none" stroke="var(--purple)" stroke-width=".8"/><path d="M2.7 4.6 L4 5.9 L6.4 3.3" fill="none" stroke="var(--purple)" stroke-width=".8"/></svg><b>L-carnitine -</b> helps convert fatty acids into energy.</p>
  <p class="abs nutrient" style="top:407px"><svg width="9" height="9" viewBox="0 0 9 9"><circle cx="4.5" cy="4.5" r="3.9" fill="none" stroke="var(--purple)" stroke-width=".8"/><path d="M2.7 4.6 L4 5.9 L6.4 3.3" fill="none" stroke="var(--purple)" stroke-width=".8"/></svg><b>Chromium -</b> helps move sugars from the blood system, and turn fats, carbs, and proteins into energy.</p>

  <h3 class="abs benefits-title">OVERALL BENEFITS:</h3>
  <svg class="abs benefits-rule" width="213" height="20"><polyline points="0,19 129,19 136,4 212,4" fill="none" stroke="var(--purple)" stroke-width=".8"/></svg>

  <p class="abs benefit" style="top:482px"><svg width="8" height="8" viewBox="0 0 8 8"><path d="M1 4.3 L3 6.5 L7 1.5" fill="none" stroke="var(--purple)" stroke-width="1"/></svg>B12 helps aid in red blood cell formation and in DNA synthesis</p>
  <p class="abs benefit" style="top:513px"><svg width="8" height="8" viewBox="0 0 8 8"><path d="M1 4.3 L3 6.5 L7 1.5" fill="none" stroke="var(--purple)" stroke-width="1"/></svg>Aids in the healthy maintenance of the immune and nervous systems, and the optic nerve</p>
  <p class="abs benefit" style="top:545px"><svg width="8" height="8" viewBox="0 0 8 8"><path d="M1 4.3 L3 6.5 L7 1.5" fill="none" stroke="var(--purple)" stroke-width="1"/></svg>Helps improve skin tone, and strengthen nails and hair</p>
  <p class="abs benefit" style="top:575px"><svg width="8" height="8" viewBox="0 0 8 8"><path d="M1 4.3 L3 6.5 L7 1.5" fill="none" stroke="var(--purple)" stroke-width="1"/></svg>Boosts metabolism and energy (which may help reduce craving and encourage weight loss)</p>
  <p class="abs benefit" style="top:605px"><svg width="8" height="8" viewBox="0 0 8 8"><path d="M1 4.3 L3 6.5 L7 1.5" fill="none" stroke="var(--purple)" stroke-width="1"/></svg>Helps relieve cramping and bloating</p>
  <p class="abs benefit" style="top:627px"><svg width="8" height="8" viewBox="0 0 8 8"><path d="M1 4.3 L3 6.5 L7 1.5" fill="none" stroke="var(--purple)" stroke-width="1"/></svg>Improves memory (which may protect against Alzheimers)</p>
  <p class="abs benefit" style="top:657px"><svg width="8" height="8" viewBox="0 0 8 8"><path d="M1 4.3 L3 6.5 L7 1.5" fill="none" stroke="var(--purple)" stroke-width="1"/></svg>Enhances mood and lessens the effects of depression</p>
</section>

</body>
</html>
```